Flyer-Design für Mittagsbelieferung
Zielgruppe
Mittags Belieferung ältere Menschen, Firmen, Berufstätige
Aufgabenstellung
Text aus Datei den Bestellzettel nicht weiter beachten nur Seite 2 u.3... Logo vielleicht vorne drauf... Format bin ich unentschieden

```html
<!DOCTYPE html>
<html lang="de">
<head>
<meta charset="utf-8">
<title>pilvo bringt's – Flyer</title>
<link rel="stylesheet" href="https://fonts.googleapis.com/css2?family=Questrial&family=Roboto+Condensed:wght@400;700&family=Kaushan+Script&display=swap">
<style>
  :root {
    --stage: #8f8d76;
    --paper: #ffffff;
    --ink: #1c1c1c;
    --green: #3fa845;
    --red: #c01a1a;
    --tomato: #c8321f;
    --meat: #5b3522;
    --leaf: #6fae3c;
    --taco: #d9a94a;
    --coffee: #e9ddd0;
  }
  * { margin: 0; padding: 0; box-sizing: border-box; }
  html, body { width: 1200px; height: 1200px; overflow: hidden; }
  body { background: var(--stage); font-family: "Questrial", sans-serif; color: var(--ink); position: relative; }

  .panel { position: absolute; top: 59px; width: 510px; height: 1082px; background: var(--paper); overflow: hidden; }
  .panel--front { left: 74px; }
  .panel--back { left: 615px; }
  .hero { position: absolute; left: 0; top: 0; width: 510px; height: 540px; display: block; }

  /* front */
  .brand { position: absolute; top: 556px; width: 100%; text-align: center; font-size: 30px; color: var(--green); }
  .tagline { position: absolute; top: 596px; width: 100%; text-align: center; font-family: "Kaushan Script", cursive; font-size: 19px; }
  .mascot { position: absolute; left: 158px; top: 630px; width: 200px; height: 192px; border-radius: 50%;
    background: radial-gradient(circle at 50% 45%, #e98a3a 0%, #d34a3a 45%, #f4f4f4 72%); }
  .front-phone { position: absolute; top: 826px; width: 100%; text-align: center; font-family: "Kaushan Script", cursive; font-size: 26px; }
  .area { position: absolute; top: 894px; width: 100%; text-align: center; font-size: 14.5px; line-height: 20px; }
  .address { position: absolute; top: 1030px; width: 100%; text-align: center; font-size: 15px; word-spacing: 2px; }

  /* back */
  .price-badge { position: absolute; left: 239px; top: 324px; width: 228px; height: 228px; border-radius: 50%; background: var(--red);
    color: #fff; text-align: center; font-family: "Roboto Condensed", sans-serif; padding-top: 40px; }
  .price-badge__title { font-family: "Questrial", sans-serif; font-size: 20px; font-weight: 700; line-height: 20px; }
  .price-badge__sub { font-size: 13px; line-height: 15px; }
  .price-badge__amount { font-size: 46px; font-weight: 700; line-height: 54px; margin-top: 2px; }
  .price-badge__note { font-size: 12.5px; line-height: 16px; }

  .copy { position: absolute; left: 48px; width: 428px; font-size: 14.5px; line-height: 20px; text-align: justify; }
  .copy--intro { top: 578px; }
  .copy--invite { top: 812px; }
  .pay { position: absolute; top: 674px; font-size: 14.5px; line-height: 20px; width: 190px; }
  .pay--cash { left: 49px; }
  .pay--invoice { left: 269px; }
  .pay h3 { font-size: 14.5px; font-weight: 700; }
  .hours { position: absolute; left: 40px; top: 913px; width: 168px; text-align: right; font-size: 14.5px; line-height: 20px; }
  .divider { position: absolute; left: 238px; top: 912px; width: 2px; height: 82px; background: var(--red); }
  .hotline { position: absolute; left: 268px; top: 913px; font-family: "Roboto Condensed", sans-serif; }
  .hotline__label { font-family: "Questrial", sans-serif; font-size: 17px; font-weight: 700; }
  .hotline__number { font-size: 29px; font-weight: 700; line-height: 32px; }
  .hotline__mail { font-size: 16px; }
  .cutoff { position: absolute; top: 1028px; width: 100%; text-align: center; font-size: 14px; }
</style>
</head>
<body>

<section class="panel panel--front">
  <svg class="hero" viewBox="0 0 510 540" aria-hidden="false">
    <defs>
      <linearGradient id="pasta" x1="0" y1="0" x2="0" y2="1"><stop offset="0" stop-color="#6b4a36"/><stop offset=".45" stop-color="var(--tomato)"/><stop offset="1" stop-color="#e8c27a"/></linearGradient>
      <linearGradient id="steak" x1="0" y1="0" x2="0" y2="1"><stop offset="0" stop-color="#8a6a50"/><stop offset=".4" stop-color="var(--meat)"/><stop offset="1" stop-color="#3b2418"/></linearGradient>
      <linearGradient id="salad" x1="0" y1="0" x2="0" y2="1"><stop offset="0" stop-color="#3e7a2a"/><stop offset=".6" stop-color="var(--leaf)"/><stop offset="1" stop-color="#eef0e8"/></linearGradient>
    </defs>
    <rect role="img" aria-label="Foto: Spaghetti mit Tomatensauce und Basilikum" x="0" y="0" width="153" height="540" fill="url(#pasta)"/>
    <rect role="img" aria-label="Foto: gegrilltes Steak mit Rosmarin" x="155" y="0" width="181" height="540" fill="url(#steak)"/>
    <rect role="img" aria-label="Foto: frischer Salat mit Öl" x="338" y="0" width="172" height="540" fill="url(#salad)"/>
    <path d="M0,487 C140,480 300,425 510,442 L510,540 L0,540 Z" fill="var(--green)"/>
    <path d="M0,525 C170,515 320,470 510,482 L510,540 L0,540 Z" fill="var(--paper)"/>
  </svg>
  <div class="brand">pilvo bringt's</div>
  <div class="tagline">ihr mobiler Mittagstisch aus Gägelow</div>
  <div class="mascot" role="img" aria-label="Illustration: Maskottchen auf rotem Motorroller mit Essenstablett"></div>
  <div class="front-phone">03841/5507320</div>
  <p class="area">Derzeitiges Auslieferungsgebiet<br>Gägelow-Proseken-Barnekow-Zierow-Gressow-Stofferdorf-<br>Woltersdorf- Wismar- Neuburg -Hornstorf -Kritzow<br>auch weitere möglich</p>
  <p class="address">Pilvo-Restaurant &nbsp;|&nbsp; Lindenweg 4 &nbsp;|&nbsp; 23968 Gägelow</p>
</section>

<section class="panel panel--back">
  <svg class="hero" viewBox="0 0 510 540">
    <defs>
      <linearGradient id="taco" x1="0" y1="0" x2="0" y2="1"><stop offset="0" stop-color="#e7c25a"/><stop offset=".4" stop-color="var(--tomato)"/><stop offset=".75" stop-color="var(--taco)"/><stop offset="1" stop-color="#5a3a22"/></linearGradient>
      <linearGradient id="chicken" x1="0" y1="0" x2="0" y2="1"><stop offset="0" stop-color="#d9d2c6"/><stop offset=".25" stop-color="#4a2a18"/><stop offset=".7" stop-color="#a5522a"/><stop offset="1" stop-color="#3a2418"/></linearGradient>
      <linearGradient id="coffee" x1="0" y1="0" x2="0" y2="1"><stop offset="0" stop-color="#b58a5a"/><stop offset=".35" stop-color="#d8b48a"/><stop offset=".55" stop-color="var(--coffee)"/><stop offset="1" stop-color="#f6f6f6"/></linearGradient>
    </defs>
    <rect role="img" aria-label="Foto: Tacos mit Hackfleisch, Tomate und Salat" x="0" y="0" width="170" height="540" fill="url(#taco)"/>
    <rect role="img" aria-label="Foto: gegrilltes Hähnchenfleisch mit Rosmarin" x="172" y="0" width="178" height="540" fill="url(#chicken)"/>
    <rect role="img" aria-label="Foto: Cappuccino mit Gebäck" x="352" y="0" width="158" height="540" fill="url(#coffee)"/>
    <path d="M0,487 C140,480 300,425 510,442 L510,540 L0,540 Z" fill="var(--green)"/>
    <path d="M0,525 C170,515 320,470 510,482 L510,540 L0,540 Z" fill="var(--paper)"/>
  </svg>
  <div class="price-badge">
    <div class="price-badge__title">Preis pro Menü</div>
    <div class="price-badge__sub">inkl. Nachtisch &amp; Lieferung</div>
    <div class="price-badge__amount">6,00 €</div>
    <div class="price-badge__note">+ 1 Stück selbstgebackenen<br>Kuchen liefern wir ihnen gerne<br>für 1,50€ mit dazu</div>
  </div>
  <p class="copy copy--intro">Wir liefern Ihnen gerne Ihr Wunschmenü in unseren Thermoboxen zu Ihnen nach Hause oder auch ins Büro oder Ihren Arbeitsplatz. Sie haben täglich die Wahl zwischen 3 Menüs inkl. Nachtisch. Bei der Bezahlung haben Sie die Wahl zwischen</p>
  <div class="pay pay--cash"><h3>Barzahlung</h3>immer Montags im Vorraus beim Fahrer gegen Erhalt der Wochenrechnung</div>
  <div class="pay pay--invoice"><h3>Monatsrechnung</h3>am Ende des Monats wird ihnen eine Rechnung für den jeweiligen Monat ausgestellt die Sie dann einfach über-weisen.</div>
  <p class="copy copy--invite">Fordern sie noch heute einen Speiseplan von uns an, und lassen Sie sich von unseren täglich frisch zubereiteten Speisen überzeugen. Keine Vertragsbindung!! d.h. Sollte es ihnen nicht gefallen können Sie jederzeit wieder abbestellen</p>
  <p class="hours">Auslieferung erfolgt von<br>Montag - Samstag<br>zwischen 10.30 Uhr<br>und 12.30 Uhr</p>
  <div class="divider"></div>
  <div class="hotline">
    <div class="hotline__label">Bestellhotline</div>
    <div class="hotline__number">03841/5507320</div>
    <div class="hotline__mail">oder mail an pilvo@postfeld.de</div>
  </div>
  <p class="cutoff">An-und Abbestellungen sind täglich bis 10.00Uhr möglich</p>
</section>

</body>
</html>
```